Maple Dental of Temecula needs a flyer

We need a flyer design for Maple Dental. We are located in the city of Temecula in California. Our dental office does general dentistry, cosmetic dentistry, dental implants, orthodontics, dental sleep apnea and TMJ treatment. We would like to design a flyer that could allow the reader know about our services and let them know that we accept new patients. We also have a new patient special that would included necessary dental x rays and dental exam for only $65. We do accept all major credit cards. Also our office accepts most PPO insurances. You can use some of the photos that are included or use stock photos of the dental procedure (they could be before/after photos).

```html
<!DOCTYPE html>
<html lang="en">
<head>
<meta charset="utf-8">
<title>Maple Dental of Temecula – Flyer</title>
<link href="https://fonts.googleapis.com/css2?family=Libre+Baskerville&family=Montserrat:wght@700;800&family=Lato:wght@400;700&family=Oswald:wght@400;500;700&display=swap" rel="stylesheet">
<style>
  :root{
    --plum:#574349;
    --plum-dark:#4a3b40;
    --teal:#5eabb0;
    --teal-icon:#3f9fc4;
    --grey:#ebebeb;
    --ink:#3a3a3a;
    --page:#3b3b3b;
    --white:#ffffff;
  }
  *{margin:0;padding:0;box-sizing:border-box}
  html,body{width:1200px;height:1200px;overflow:hidden;background:var(--page)}
  .flyer{
    position:absolute;left:190px;top:18px;width:900px;height:1276px;
    background:var(--white);transform:scale(0.9122);transform-origin:top left;
    font-family:"Lato",sans-serif;color:var(--ink);overflow:hidden;
  }
  .abs{position:absolute}
  .hero-art{left:0;top:0;width:900px;height:560px}
  .headline{left:45px;top:346px;color:var(--plum-dark)}
  .headline .kicker{font-family:"Libre Baskerville",serif;font-size:27px;line-height:32px}
  .headline .you-can{font-family:"Libre Baskerville",serif;font-size:60px;line-height:66px;letter-spacing:1px}
  .headline .trust{font-family:"Montserrat",sans-serif;font-weight:800;font-size:86px;line-height:84px;letter-spacing:1px}

  .services{left:0;top:538px;width:597px;height:202px;background:var(--grey);padding:14px 38px 0 38px}
  .section-title{font-family:"Lato",sans-serif;font-size:21px;color:var(--plum-dark);letter-spacing:.5px;line-height:24px}
  .services p{font-size:13.6px;line-height:16.5px;margin-top:8px;width:525px}
  .service-grid{display:grid;grid-template-columns:184px 206px 150px;row-gap:18px;margin-top:12px;margin-left:2px}
  .service{display:flex;align-items:center;gap:7px;font-size:13px;font-weight:700;color:var(--ink)}
  .service svg{width:22px;height:22px;flex:none}

  .compare{left:597px;top:538px;width:303px;height:127px}
  .compare .shot{position:absolute;top:0;height:99px}
  .compare .before{left:0;width:151px;background:linear-gradient(180deg,#c98a7e,#d9a89a 45%,#f1ece6 60%,#b5665c)}
  .compare .after{left:165px;width:138px;background:linear-gradient(180deg,#c98a7e,#d9a89a 45%,#ffffff 60%,#b5665c)}
  .compare .labels{position:absolute;left:0;top:99px;width:303px;height:28px;background:var(--plum);display:flex;justify-content:space-around;color:var(--white);font-size:19px;line-height:28px}

  .offer{left:597px;top:665px;width:303px;height:197px;background:var(--teal);color:var(--white);text-align:center}
  .offer .line1{font-family:"Oswald",sans-serif;font-size:30px;margin-top:22px;line-height:36px;letter-spacing:-.3px}
  .offer .line2{font-size:23px;line-height:28px}
  .offer .line2 b{font-weight:700}
  .offer .price{font-family:"Oswald",sans-serif;font-weight:700;font-size:80px;line-height:96px;margin-top:4px}

  .about{left:37px;top:744px;width:535px}
  .about p{font-size:13.6px;line-height:16.5px;margin-top:8px;text-align:justify}

  .doctor{left:40px;top:918px;width:562px}
  .doctor h2{font-family:"Montserrat",sans-serif;font-weight:700;font-size:21px;color:var(--plum-dark);letter-spacing:.3px}
  .doctor h2 span{color:var(--plum)}
  .doctor p{font-size:13.2px;line-height:16.5px;margin-top:16px;text-align:justify}
  .call{right:298px;top:1042px;font-family:"Oswald",sans-serif;font-size:28px;color:#222;letter-spacing:-.3px}

  .portrait{left:640px;top:890px;width:230px;height:310px;border-radius:40% 40% 0 0;background:linear-gradient(180deg,#4a3528,#c99a80 30%,#e7c3aa 50%,#2a2a2a 78%,#1e1e1e)}
  .footer-art{left:0;top:1050px;width:900px;height:226px}
  .contact{top:1216px;display:flex;align-items:center;gap:12px;color:var(--white);font-size:14px}
  .contact svg{width:20px;height:20px}
</style>
</head>
<body>
<div class="flyer">
  <svg class="abs hero-art" viewBox="0 0 900 560" aria-hidden="true">
    <defs>
      <linearGradient id="heroFill" x1="0" y1="0" x2="1" y2="0">
        <stop offset="0" stop-color="#7fa8c8"/>
        <stop offset=".35" stop-color="#1f5fa8"/>
        <stop offset=".65" stop-color="#e4b8a5"/>
        <stop offset="1" stop-color="#5a3a30"/>
      </linearGradient>
    </defs>
    <rect width="900" height="470" fill="url(#heroFill)" role="img" aria-label="Photo of a smiling patient with a dentist holding dental tools"/>
    <path d="M0,338 C120,255 300,240 480,300 C650,360 780,445 900,405 L900,560 L0,560 Z" fill="var(--white)"/>
    <path d="M120,287 C300,240 460,290 600,368 C690,418 740,446 778,452 C690,455 610,425 520,378 C400,318 260,280 120,287 Z" fill="var(--plum)"/>
  </svg>

  <div class="abs headline">
    <div class="kicker">Complete Dental Care</div>
    <div class="you-can">YOU CAN</div>
    <div class="trust">TRUST</div>
  </div>

  <section class="abs services">
    <h2 class="section-title">SERVICES</h2>
    <p>Whether you need a routine cleaning and checkup or more comprehensive dental work done, Maple Dental has you covered. We provide an expansive list of general dentistry services to our valued clients. We commonly provide the following dental services.</p>
    <div class="service-grid">
      <div class="service"><svg viewBox="0 0 24 24"><path d="M4 18 L14 8 L17 11 L7 21 Z M15 4 l5 5" stroke="var(--teal-icon)" stroke-width="2.4" fill="var(--teal-icon)"/></svg>General Dentistry</div>
      <div class="service"><svg viewBox="0 0 24 24"><path d="M6 3c3 0 4 1 6 1s3-1 6-1c3 1 3 5 1 9-1 3-1 9-3 9s-2-6-4-6-2 6-4 6-2-6-3-9C3 8 3 4 6 3z" fill="var(--teal-icon)"/></svg>Cosmetic Dentistry</div>
      <div class="service"><svg viewBox="0 0 24 24"><path d="M5 3h14c0 5-3 6-7 6S5 8 5 3z M9 11h6 M9 14h6 M10 17h4 M11 20h2" stroke="var(--teal-icon)" stroke-width="1.8" fill="none"/></svg>Dental Implants</div>
      <div class="service"><svg viewBox="0 0 24 24"><path d="M6 3c3 0 4 1 6 1s3-1 6-1c3 1 3 5 1 9-1 3-1 9-3 9s-2-6-4-6-2 6-4 6-2-6-3-9C3 8 3 4 6 3z M8 10h8" stroke="var(--teal-icon)" stroke-width="1.5" fill="none"/></svg>Orthodontics</div>
      <div class="service"><svg viewBox="0 0 24 24"><path d="M2 19V9 M2 15h20v4 M5 13h5v-2H5z M11 13h10v-2H11z M16 4h3l-3 3h3" stroke="var(--teal-icon)" stroke-width="1.8" fill="none"/></svg>Dental Sleep Apnea</div>
      <div class="service"><svg viewBox="0 0 24 24"><circle cx="12" cy="12" r="8" fill="var(--teal-icon)"/><path d="M9 10h6" stroke="#fff" stroke-width="2"/></svg>TMJ treatment</div>
    </div>
  </section>

  <div class="abs compare">
    <div class="shot before" role="img" aria-label="Before photo of a smile with gapped teeth"></div>
    <div class="shot after" role="img" aria-label="After photo of a smile with even white teeth"></div>
    <div class="labels"><span>before</span><span>after</span></div>
  </div>

  <div class="abs offer">
    <div class="line1">Necessary dental x rays</div>
    <div class="line2">and dental examfor <b>only</b></div>
    <div class="price">$65</div>
  </div>

  <section class="abs about">
    <h2 class="section-title">ABOUT US</h2>
    <p>Maple Dental is a comprehensive PPO insurance family dentistry practice serving the Temecula | Murrieta | Menifee | Fallbrook | Riverside County areas. Dr. Darius Kalani, DDS is a PCU graduate and brings over 20 years of experience to this high-quality practice. Additionally, our office staff and dental assistants are friendly knowledgeable and attentive. We strive to provide our patients with exceptional dental care in a relaxed, comfortable atmosphere.</p>
  </section>

  <section class="abs doctor">
    <h2>Darius Kalani, <span>DDS, FIAO, DADIA, ICOI</span></h2>
    <p>Dr. Kalani’s education began with his undergraduate degree in Chemical Engineering from Eastbrook University. Inspired by his father’s career as a physician, Dr. Kalani decided to pursue a career in Dentistry. He graduated from the Pacific Coast University Dental School in 1993 and practiced general dentistry for several years.</p>
  </section>

  <div class="abs call">CALL US (951) 555-0142</div>

  <div class="abs portrait" role="img" aria-label="Portrait photo of the dentist in a dark suit"></div>

  <svg class="abs footer-art" viewBox="0 0 900 226" aria-hidden="true">
    <path d="M0,28 C140,5 260,10 330,72 C250,40 130,42 0,70 Z" fill="var(--teal)"/>
    <path d="M0,100 C160,40 360,45 520,105 C690,165 820,115 900,18 L900,226 L0,226 Z" fill="var(--plum)"/>
  </svg>

  <div class="abs contact" style="left:38px">
    <svg viewBox="0 0 24 24"><path d="M12 2a6 6 0 0 0-6 6c0 5 6 12 6 12s6-7 6-12a6 6 0 0 0-6-6z" fill="none" stroke="#fff" stroke-width="1.8"/><circle cx="12" cy="8" r="2" fill="#fff"/><path d="M5 22h14" stroke="#fff" stroke-width="1.8"/></svg>
    <span>41280 Vineyard Crest Road #210 Temecula CA 92591</span>
  </div>
  <div class="abs contact" style="left:445px">
    <svg viewBox="0 0 24 24"><path d="M3 10l9-6 9 6v10H3z M3 10l9 6 9-6" fill="none" stroke="#fff" stroke-width="1.8"/></svg>
    <span>office@maple-dental.com</span>
  </div>
  <div class="abs contact" style="left:675px">
    <svg viewBox="0 0 24 24"><circle cx="12" cy="12" r="9" fill="none" stroke="#fff" stroke-width="1.8"/><path d="M3 12h18 M12 3c-4 5-4 13 0 18 M12 3c4 5 4 13 0 18" fill="none" stroke="#fff" stroke-width="1.4"/></svg>
    <span>www.maple-dental.com</span>
  </div>
</div>
</body>
</html>
```